Innovative Bitcoin Powerpoint Presentation

I have constructred most of the data for a 15 page powerpoint presentation on an innovative bitcoin idea that provides access to fiat currency with bitcoin hodlings

I need this to look great as a first blush to potential investors

Reason: updated deck and name

Target Market(s)

Venture Capital firms and private equity firms

Requirements
Must have
• Fun, innovateive deck, very clean
Should not have
• any generic feel - no templates

```html
<!DOCTYPE html>
<html lang="en">
<head>
<meta charset="utf-8">
<title>Fiatline — Investor Deck Overview</title>
<link href="https://fonts.googleapis.com/css2?family=Lato:wght@300;400;700&family=Montserrat:wght@500;600;700&display=swap" rel="stylesheet">
<style>
  :root {
    --canvas-bg: #a7b4b9;
    --gold: #e0b176;
    --gold-mid: #d6a96f;
    --gold-dark: #b08a5e;
    --gold-soft: #eac79b;
    --teal: #467a71;
    --teal-deep: #2f5a52;
    --teal-band: #3a5f59;
    --teal-ink: #2f5550;
    --header-bg: #f4f4f4;
    --ink: #2b2b2b;
    --white: #ffffff;
  }
  * { margin: 0; padding: 0; box-sizing: border-box; }
  html, body { width: 1063px; height: 1200px; overflow: hidden; background: var(--canvas-bg); }
  .deck { position: relative; width: 1063px; height: 1200px; }
  .slide { position: absolute; width: 516px; height: 385px; overflow: hidden; background: var(--white); }
  .slide svg { display: block; width: 516px; height: 385px; }
  .slide--cover { left: 12px; top: 11px; }
  .slide--title { left: 537px; top: 11px; }
  .slide--overview { left: 12px; top: 407px; }
  .slide--solution { left: 537px; top: 407px; }
  .slide--relationship { left: 12px; top: 804px; }
  .slide--contact { left: 537px; top: 804px; }

  .brand { font-family: "Montserrat", sans-serif; font-weight: 500; }
  .brand-bold { font-family: "Montserrat", sans-serif; font-weight: 600; }
  .body { font-family: "Lato", sans-serif; font-weight: 400; }
  .light { font-family: "Lato", sans-serif; font-weight: 300; }
  .strong { font-family: "Lato", sans-serif; font-weight: 700; }
  .slide-title { font-family: "Lato", sans-serif; font-weight: 300; font-size: 24px; fill: var(--gold); }
</style>
</head>
<body>
<main class="deck">

  <!-- Cover -->
  <section class="slide slide--cover">
    <svg viewBox="0 0 582 435">
      <defs>
        <radialGradient id="coverGlow" cx="0.5" cy="0.5" r="0.75">
          <stop offset="0" stop-color="#e4b67d"/>
          <stop offset="1" stop-color="#98744c"/>
        </radialGradient>
      </defs>
      <rect class="cover-bg" width="582" height="435" fill="url(#coverGlow)"/>
      <circle class="brand-dot" cx="292" cy="184" r="54" fill="none" stroke="var(--white)" stroke-width="10"/>
      <text class="brand" x="291" y="309" font-size="58" fill="var(--white)" text-anchor="middle">Fiatline</text>
    </svg>
  </section>

  <!-- Title -->
  <section class="slide slide--title">
    <svg viewBox="0 0 582 435">
      <circle class="brand-dot" cx="291" cy="123" r="44" fill="none" stroke="var(--gold)" stroke-width="9"/>
      <text class="brand" x="291" y="228" font-size="50" fill="var(--teal-ink)" text-anchor="middle">Fiatline</text>
      <text class="body" x="558" y="304" font-size="19" fill="var(--ink)" text-anchor="end">PRESENTATION TITLE</text>
      <text class="body" x="558" y="321" font-size="11" fill="var(--gold)" text-anchor="end">JAN 2014</text>
      <rect class="presenter-band" x="0" y="350" width="582" height="82" fill="var(--teal-band)"/>
      <rect x="0" y="432" width="582" height="3" fill="var(--gold)"/>
      <text x="22" y="388" font-size="20" fill="var(--white)"><tspan class="strong">MARCUS</tspan><tspan class="light"> R. DELANE</tspan></text>
      <text x="24" y="407" font-size="11" class="body" fill="var(--gold)">to <tspan class="strong">Business</tspan>/Client</text>
    </svg>
  </section>

  <!-- Overview -->
  <section class="slide slide--overview">
    <svg viewBox="0 0 582 435">
      <defs>
        <linearGradient id="funnelTone" x1="0" y1="0" x2="0" y2="1">
          <stop offset="0" stop-color="#7fa39b"/>
          <stop offset="1" stop-color="var(--gold-soft)"/>
        </linearGradient>
      </defs>
      <rect class="slide-header" width="582" height="39" fill="var(--header-bg)"/>
      <text class="slide-title" x="10" y="28">Overview</text>

      <rect class="funnel-illustration" x="39" y="48" width="264" height="258" fill="url(#funnelTone)"
            role="img" aria-label="Illustration: digital wallet, debit card and line of credit bubbles dropping into a funnel"/>
      <path d="M166 309 h10 v9 h7 l-12 11 l-12 -11 h7 Z" fill="var(--teal)"/>
      <circle cx="171" cy="347" r="11" fill="none" stroke="var(--gold)" stroke-width="2.5"/>
      <text class="brand" x="171" y="377" font-size="14" fill="var(--teal-ink)" text-anchor="middle">Fiatline</text>

      <g class="value-chain">
        <rect x="355" y="65" width="186" height="49" fill="var(--gold)"/>
        <text class="body" x="448" y="93" font-size="9" fill="var(--white)" text-anchor="middle">Scalable Technology</text>
        <path d="M443 115 h10 v10 h7 l-12 12 l-12 -12 h7 Z" fill="var(--teal)"/>
        <rect x="355" y="152" width="186" height="49" fill="var(--gold)"/>
        <text class="body" x="448" y="180" font-size="9" fill="var(--white)" text-anchor="middle">Lower Transaction Cost</text>
        <path d="M443 202 h10 v10 h7 l-12 12 l-12 -12 h7 Z" fill="var(--teal)"/>
        <rect x="355" y="239" width="186" height="49" fill="var(--gold)"/>
        <text class="body" x="448" y="267" font-size="9" fill="var(--white)" text-anchor="middle">First Mover Advantage</text>
        <path d="M443 289 h10 v10 h7 l-12 12 l-12 -12 h7 Z" fill="var(--teal)"/>
        <rect x="355" y="327" width="186" height="49" fill="var(--gold)"/>
        <text class="body" x="448" y="355" font-size="9" fill="var(--white)" text-anchor="middle">Global Opportunity</text>
      </g>

      <g class="slide-footer">
        <rect y="398" width="582" height="37" fill="var(--teal-band)"/>
        <circle cx="22" cy="417" r="7" fill="none" stroke="var(--white)" stroke-width="2"/>
        <text class="brand-bold" x="34" y="422" font-size="14" fill="var(--white)">Fiatline</text>
        <text class="body" x="557" y="424" font-size="9" fill="var(--gold)" text-anchor="middle">3</text>
      </g>
    </svg>
  </section>

  <!-- Solution -->
  <section class="slide slide--solution">
    <svg viewBox="0 0 582 435">
      <rect class="slide-header" width="582" height="39" fill="var(--header-bg)"/>
      <text class="slide-title" x="10" y="28">Solution</text>

      <text class="body" x="121" y="107" font-size="12.5" fill="var(--ink)" text-anchor="middle">Leverages BTC as collateral</text>
      <line x1="115" y1="113" x2="115" y2="150" stroke="var(--teal-ink)" stroke-width="1"/>
      <path d="M112 148 L115 154 L118 148 Z" fill="var(--teal-ink)"/>
      <text class="body" x="458" y="107" font-size="12.5" fill="var(--ink)" text-anchor="middle">+ relationship between BTC and cash</text>
      <line x1="457" y1="113" x2="457" y2="150" stroke="var(--teal-ink)" stroke-width="1"/>
      <path d="M454 148 L457 154 L460 148 Z" fill="var(--teal-ink)"/>

      <circle cx="115" cy="222" r="67" fill="var(--gold)"/>
      <text class="body" x="115" y="218" font-size="14" fill="var(--white)" text-anchor="middle">Secured line of</text>
      <text class="body" x="115" y="236" font-size="14" fill="var(--white)" text-anchor="middle">credit</text>
      <text class="light" x="199" y="232" font-size="30" fill="var(--ink)" text-anchor="middle">+</text>
      <circle cx="284" cy="222" r="67" fill="var(--gold-mid)"/>
      <text class="body" x="284" y="218" font-size="14" fill="var(--white)" text-anchor="middle">Fiatline</text>
      <text class="body" x="284" y="236" font-size="14" fill="var(--white)" text-anchor="middle">Debit Card</text>
      <text class="light" x="368" y="232" font-size="30" fill="var(--ink)" text-anchor="middle">=</text>
      <circle cx="453" cy="222" r="67" fill="var(--teal)"/>
      <text class="body" x="453" y="228" font-size="14" fill="var(--white)" text-anchor="middle">Operating leverage</text>

      <line x1="284" y1="309" x2="284" y2="345" stroke="var(--teal-ink)" stroke-width="1"/>
      <path d="M281 311 L284 305 L287 311 Z" fill="var(--teal-ink)"/>
      <text class="body" x="284" y="365" font-size="12.5" fill="var(--ink)" text-anchor="middle">Global access to local currency</text>

      <g class="slide-footer">
        <rect y="398" width="582" height="37" fill="var(--teal-band)"/>
        <circle cx="22" cy="417" r="7" fill="none" stroke="var(--white)" stroke-width="2"/>
        <text class="brand-bold" x="34" y="422" font-size="14" fill="var(--white)">Fiatline</text>
        <text class="body" x="557" y="424" font-size="9" fill="var(--gold)" text-anchor="middle">5</text>
      </g>
    </svg>
  </section>

  <!-- Cash vs Coin -->
  <section class="slide slide--relationship">
    <svg viewBox="0 0 582 435">
      <rect class="slide-header" width="582" height="39" fill="var(--header-bg)"/>
      <text class="slide-title" x="10" y="28">Cash Vs. Coin Relationship</text>

      <text class="strong" x="151" y="114" font-size="14" fill="var(--teal-ink)" text-anchor="middle">Current Relationship</text>
      <circle cx="433" cy="88" r="14" fill="none" stroke="var(--gold)" stroke-width="3"/>
      <text class="brand" x="433" y="124" font-size="16" fill="var(--teal-ink)" text-anchor="middle">Fiatline</text>

      <g class="flow-arrows" fill="var(--gold)">
        <path d="M84 133 L141 181 L123 181 L123 293 L45 293 L45 181 L27 181 Z"/>
        <path d="M167 176 L245 176 L245 288 L263 288 L206 336 L149 288 L167 288 Z"/>
        <path d="M367 133 L427 181 L408 181 L408 293 L326 293 L326 181 L307 181 Z"/>
        <path d="M498 133 L555 181 L537 181 L537 293 L459 293 L459 181 L441 181 Z"/>
      </g>
      <line x1="123" y1="213" x2="167" y2="213" stroke="var(--ink)" stroke-width="1" stroke-dasharray="2 2"/>
      <line x1="408" y1="213" x2="459" y2="213" stroke="var(--ink)" stroke-width="1" stroke-dasharray="2 2"/>

      <text class="body" x="84" y="206" font-size="12" fill="var(--white)" text-anchor="middle">Buy BTC</text>
      <text class="body" x="84" y="221" font-size="12" fill="var(--white)" text-anchor="middle">with Fiat</text>
      <text class="strong" x="84" y="272" font-size="38" fill="var(--white)" text-anchor="middle">₿</text>
      <text class="strong" x="206" y="230" font-size="42" fill="var(--white)" text-anchor="middle">$</text>
      <text class="body" x="206" y="255" font-size="12" fill="var(--white)" text-anchor="middle">Sell BTC</text>
      <text class="body" x="206" y="270" font-size="12" fill="var(--white)" text-anchor="middle">for Fiat</text>
      <text class="body" x="367" y="210" font-size="12" fill="var(--white)" text-anchor="middle">Greater BTC</text>
      <text class="body" x="367" y="225" font-size="12" fill="var(--white)" text-anchor="middle">Holdings</text>
      <text class="strong" x="367" y="272" font-size="38" fill="var(--white)" text-anchor="middle">₿</text>
      <text class="body" x="498" y="210" font-size="12" fill="var(--white)" text-anchor="middle">Operating</text>
      <text class="body" x="498" y="225" font-size="12" fill="var(--white)" text-anchor="middle">leverage</text>
      <text class="strong" x="498" y="275" font-size="42" fill="var(--white)" text-anchor="middle">$</text>

      <text class="strong" x="291" y="347" font-size="9" fill="var(--teal-ink)" text-anchor="middle">Potential Relationship</text>
      <line x1="48" y1="355" x2="530" y2="355" stroke="var(--teal-ink)" stroke-width="1.2"/>
      <path d="M528 352 L535 355 L528 358 Z" fill="var(--teal-ink)"/>

      <g class="slide-footer">
        <rect y="398" width="582" height="37" fill="var(--teal-band)"/>
        <circle cx="22" cy="417" r="7" fill="none" stroke="var(--white)" stroke-width="2"/>
        <text class="brand-bold" x="34" y="422" font-size="14" fill="var(--white)">Fiatline</text>
        <text class="body" x="557" y="424" font-size="9" fill="var(--gold)" text-anchor="middle">6</text>
      </g>
    </svg>
  </section>

  <!-- Contact -->
  <section class="slide slide--contact">
    <svg viewBox="0 0 582 435">
      <defs>
        <linearGradient id="contactFade" x1="0" y1="0" x2="0" y2="1">
          <stop offset="0" stop-color="#3e6862"/>
          <stop offset="1" stop-color="#223e39"/>
        </linearGradient>
      </defs>
      <rect width="582" height="435" fill="url(#contactFade)"/>
      <circle cx="291" cy="110" r="35" fill="none" stroke="var(--white)" stroke-width="6"/>
      <text class="brand" x="291" y="192" font-size="40" fill="var(--white)" text-anchor="middle">Fiatline</text>
      <text class="body" x="291" y="260" font-size="18" fill="var(--white)" text-anchor="middle">Contact Information</text>
      <text class="strong" x="107" y="326" font-size="9" fill="var(--gold)">Contact us:</text>
      <text class="body" x="107" y="339" font-size="9" fill="var(--white)">555-010-0199</text>
      <text class="body" x="107" y="352" font-size="9" fill="var(--white)">www.fiatline.com</text>
      <text class="strong" x="371" y="326" font-size="9" fill="var(--gold)">Central Office:</text>
      <text class="body" x="371" y="339" font-size="9" fill="var(--white)">Address Line 1</text>
      <text class="body" x="371" y="352" font-size="9" fill="var(--white)">Address Line 2</text>
    </svg>
  </section>

</main>
</body>
</html>
```